Brightvale services brochure

We need a new company brochure. The brochure will be formatted for PDF distribution but should be printable on "letter" size paper. 2 pages plus front and back cover. Color white and same blue as logo. Logo "O" should be used as design. Look at webpage for general info: www.brightvale-example.ca<br/><br/>Front cover: pic1, logo, design and "Your Cleaning is Our Business". <br/>Back cover" "O" design, logo and info from "contact" page<br/>Front cover inside: design and intro from web home page, also use stock pics of clean offices ect as placeholders for purchased pics.<br/>1st page: design and "Our Services", use info of "Cleanroom & GMP Services", "Janitorial Services" from services page.<br/>2nd page: design and "Special Services", info from "Carpet & Upholstery Services", "Window Cleaning Services", and list of "Other Services".<br/>Back cover inside : design and info from technology page, use stock pics for place holders.

Industry/Entity Type

Janitorial

Font styles to use
Sans Serif
Other font styles liked:
• Futura Book

Colors
0555a3

Requirements
Must have
• The logo "O" (target) should be part of the design. Design color same as logo.

```html
<!DOCTYPE html>
<html lang="en">
<head>
<meta charset="utf-8">
<title>Brightvale — Services Brochure Spread</title>
<link href="https://fonts.googleapis.com/css2?family=Anton&family=Roboto+Condensed:ital,wght@0,700;1,700&family=Arimo:wght@400&display=swap" rel="stylesheet">
<style>
  :root{
    --blue:#0555a3;
    --navy:#0d1b3e;
    --ink:#1a1a1a;
    --page-white:#ffffff;
    --page-grey:#e6e6e8;
    --backdrop:#d9d9dc;
  }
  *{box-sizing:border-box;margin:0;padding:0}
  html,body{width:1200px;height:840px;overflow:hidden}
  body{background:var(--backdrop);display:flex;align-items:center;justify-content:center;font-family:"Arimo",Arial,sans-serif}
  .spread{display:flex;width:1120px;height:724px;box-shadow:0 10px 30px rgba(0,0,0,.18)}
  .page{position:relative;width:560px;height:724px;padding:30px 30px 24px;overflow:hidden}
  .page--services{background:var(--page-white)}
  .page--special{background:var(--page-grey)}
  .page-title{font-family:"Anton",Impact,sans-serif;font-weight:400;font-size:46px;line-height:1;letter-spacing:.5px;color:var(--navy);margin-bottom:14px}
  .page--services .page-title{text-align:center}
  .page--special .page-title{text-align:right;margin-right:20px}
  .page-title .accent{color:var(--blue)}
  .section-band{position:relative;display:inline-block;height:30px;margin-left:-30px;padding:0 28px 0 30px;
    background:linear-gradient(90deg,var(--navy) 0%,var(--navy) 52%,var(--blue) 100%);
    border-radius:0 16px 16px 0;color:#fff;font-family:"Roboto Condensed",Arial,sans-serif;font-weight:700;font-size:19px;line-height:30px;margin-bottom:10px}
  .section{overflow:hidden}
  .section + .section{margin-top:18px}
  .body-copy{font-size:9.2px;line-height:1.34;color:var(--ink);text-align:justify}
  .photo{float:right;margin:0 0 8px 14px;border:5px solid var(--blue);box-shadow:0 0 0 3px var(--navy)}
  .photo--mop{width:180px;height:118px;background:linear-gradient(135deg,#d8dde3,#9fb4c8 55%,#3a8fd0)}
  .photo--hall{width:180px;height:118px;background:linear-gradient(135deg,#c9ccd2,#7a8da3 50%,#2d6aa8)}
  .photo--supplies{width:190px;height:120px;background:linear-gradient(135deg,#f2f2f2,#cfe3c0 45%,#8fb8e0)}
  .photo--carpet{width:210px;height:112px;background:linear-gradient(135deg,#b9b2a8,#5b6470 55%,#2f3a4a)}
  .photo--floor{width:210px;height:112px;background:linear-gradient(135deg,#d9cfc2,#8fa9c0 55%,#2f7dc4)}
  .photo--window{width:220px;height:118px;background:linear-gradient(135deg,#eef0f2,#b8c6d4 55%,#3d85c6)}
  .photo-stack{float:right;margin-left:14px}
  .photo-stack .photo{float:none;margin:0 0 16px}
  .section--window .section-band{margin-top:30px}
</style>
</head>
<body>
<main class="spread">
  <section class="page page--services">
    <h1 class="page-title">OUR <span class="accent">SERVICES</span></h1>

    <article class="section">
      <h2 class="section-band">Cleanroom &amp; GMP Services</h2>
      <div class="photo photo--mop" role="img" aria-label="Photo of a cleaner mopping a floor beside a blue bucket"></div>
      <div class="photo photo--hall" role="img" aria-label="Photo of staff cleaning a controlled facility corridor" style="clear:right"></div>
      <p class="body-copy">Brightvale is a leading brand in cleanroom cleaning and boasts an impressive performance record. The company is recognized as a reliable, mature organization, continually adjusting and perfecting the systems and methodologies used to bring cleanroom cleaning procedures and technology to businesses worldwide. We service such industries as medical device manufacturers, pharmaceutical manufacturers, expanding research facilities and contract laboratories. Brightvale's cleanroom solutions suit your GMP protocols. Brightvale offers cleanroom cleaning services performed on a variable frequency. Service frequency ranges from a one-time event to daily maintenance. The scope of each service is adjusted based on the existing level of cleanliness and the target level of cleanliness. Whether your cleanroom is a small soft-wall enclosure or an entire facility, it needs to be cleaned in order to maintain the process or product yield. Brightvale will follow your established GMP protocols for cleaning all areas of your cleanroom. If necessary, Brightvale will collaborate with you to establish the best cleaning protocols. Brightvale technicians can perform all aspects of cleanroom cleaning — from construction cleaning to daily maintenance. Whether your cleanroom is Class A, B, C, D, sterile or non-sterile, Brightvale can clean it, and keep it clean.</p>
    </article>

    <article class="section">
      <h2 class="section-band">Janitorial Services</h2>
      <div class="photo photo--supplies" role="img" aria-label="Photo of a caddy holding spray bottles, gloves and cleaning tools"></div>
      <p class="body-copy">Brightvale provides complete janitorial services for any type/size operation. We currently service the public and private sectors: offices, financial institutions, industrial plants, schools, apartment buildings, showrooms, churches, as well as many other facilities. Our project fulfilment is flexible and entirely tailored to your needs. We ensure that our staff is properly trained and fully equipped to professionally complete the job efficiently, the first time. Moreover, your job will be inspected by one of our highly skilled "hands on" supervisors. As a member of the Northern Facility Care Council and the Global Cleaning Standards Guild, Brightvale pledges to adhere to the strict code of ethics established by the cleaning and building services industry. We take on jobs as diverse as sweeping sidewalks, gum removal from furniture, sidewalks and structural surfaces, even sanitizing foul smells formed around your building and providing power washing of building interiors and exteriors, sidewalks and parking areas.</p>
    </article>
  </section>

  <section class="page page--special">
    <h1 class="page-title">SPECIAL <span class="accent">SERVICES</span></h1>

    <article class="section">
      <h2 class="section-band">Carpet &amp; Upholstery Services</h2>
      <div class="photo-stack">
        <div class="photo photo--carpet" role="img" aria-label="Photo of a carpet being cleaned with an extraction wand"></div>
        <div class="photo photo--floor" role="img" aria-label="Photo of a mop and blue bucket on a hard floor"></div>
      </div>
      <p class="body-copy">Office furnishings such as carpets, drapes and upholstered furniture represent a serious investment to a company. We maintain this investment with care and quality that extends the lifespan of furniture and carpet. Where many of our competitors offer a narrow range of cleaning and maintenance options, Brightvale utilizes specialized equipment at any given location. This means that your furnishings will be handled appropriately, taking into consideration the varying soiling conditions, type of carpeting or fabric, in addition to responding to weight, color, backing, underlay and texture. In other words, you get the cleaning method that's best for you! In high traffic areas Rotary Shampooing techniques remove stubborn stains. Steam Cleaning and Hot Water Extraction techniques clean and flush grit and residue to thoroughly clean carpets deep into their core. Bonnet Buff systems spray and massage carpets removing emulsified dirt. Pile Lifting, Dry Cleaning and straight vacuuming is also used where appropriate and effective. Care of upholstered furniture is just as rigorous. We are able to service all materials and fabrics using shampoo, steam cleaning and dry cleaning techniques that are appropriate. To ensure the longevity of your carpet and upholstery, we use state of the art Fiber Protection Systems. Our objective is to provide you with the cleanest possible surfaces while at the same time assure the safest results.</p>
    </article>

    <article class="section section--window">
      <div class="photo photo--window" role="img" aria-label="Photo of a cleaner wiping a window with a blue cloth"></div>
      <h2 class="section-band">Window Cleaning Services</h2>
      <p class="body-copy" style="clear:right">We can implement a regular program of interior and exterior window cleaning, or we can meet your needs as a project basis. We have the staff and equipment to tackle both high-rise and low level window cleaning. In addition to windows, we are also prepared to handle all your awning and canopy sign cleaning needs, as well as lighting element replacement when required. Brightvale has built its impressive customer list by satisfying every challenge building management has passed our way.</p>
    </article>
  </section>
</main>
</body>
</html>
```